The Quillmore Daily Ledger

I am making a journal for tracking pain symptoms for TMJ (Jaw) pain. I have the cover designed and I just need the journal page designed that will repeat throughout the journal. The journal is the image on the left of the bundle. The page I would like to be developed is the picture that I hand sketched out. It should be a 6 x 9 page, similar to the attached example. Greyscale, no color. Thank you!

Target Market(s)

20-55 year old women

Industry/Entity Type

Healthcare

Colors

Designer to choose only greyscale colors for use in the design.

Requirements
Must have
• A neat, well-designed page with the content I have sketched out by hand.
Nice to have
• Creative display of the content I provided and development of the pain scale and pain diagram faces in a professional looking way.

```html
<!DOCTYPE html>
<html lang="en">
<head>
<meta charset="utf-8">
<title>Daily Jaw Pain Log Page</title>
<link href="https://fonts.googleapis.com/css2?family=Questrial&family=Jost:wght@500;600&family=Roboto+Condensed:wght@400&display=swap" rel="stylesheet">
<style>
  :root{
    --backdrop:#7a7a7a;
    --paper:#ffffff;
    --ink:#2b2b2b;
    --band:#333436;
    --row-dark:#bdbdbd;
    --row-light:#e7e7e7;
    --line:#222;
    --mid:#555;
  }
  *{box-sizing:border-box;margin:0;padding:0}
  html,body{width:1200px;height:1200px;overflow:hidden;background:var(--backdrop)}
  .page{position:absolute;left:220px;top:30px;width:855px;height:1283px;background:var(--paper);
    transform:scale(.8885);transform-origin:top left;color:var(--ink);
    font-family:"Questrial",sans-serif}
  .abs{position:absolute}
  .band{position:absolute;left:35px;width:785px;height:41px;background:var(--band);color:#fff;
    font-family:"Jost",sans-serif;font-weight:500;font-size:22px;letter-spacing:.5px;
    display:flex;align-items:center;justify-content:center}
  .field{position:absolute;top:46px;font-size:19px;font-family:"Roboto Condensed",sans-serif;font-weight:400;display:flex;align-items:flex-end;gap:10px}
  .field span.rule{display:block;border-bottom:1.5px solid var(--line);height:14px}
  table.time{position:absolute;left:35px;top:120px;width:785px;border-collapse:collapse;font-family:"Roboto Condensed",sans-serif;font-size:18px}
  table.time td{border:1.5px solid var(--line);height:37px;padding-left:18px;color:#444}
  .scale{position:absolute;left:35px;top:336px;width:785px;height:140px}
  .num{position:absolute;top:0;width:32px;height:32px;border-radius:50%;background:var(--band);color:#fff;
    font-family:"Jost",sans-serif;font-size:20px;display:flex;align-items:center;justify-content:center;transform:translateX(-50%)}
  .face{position:absolute;top:43px;width:56px;height:56px;border-radius:50%;background:linear-gradient(#eee,#cfcfcf);border:3px solid var(--band);transform:translateX(-50%)}
  .level{position:absolute;top:104px;font-family:"Roboto Condensed",sans-serif;font-size:16px;text-align:center;line-height:18px;transform:translateX(-50%);white-space:nowrap}
  .loc{position:absolute;top:530px;width:100px;height:100px;transform:translateX(-50%);background:radial-gradient(circle at 50% 45%,#f0f0f0,#d2d2d2);border-radius:10px}
  .loc-label{position:absolute;top:652px;font-family:"Jost",sans-serif;font-weight:500;font-size:22px;transform:translateX(-50%)}
  .divider{position:absolute;top:535px;height:140px;border-left:1px solid #ccc}
  .q{position:absolute;left:567px;font-family:"Jost",sans-serif;font-weight:500;font-size:19px;line-height:24px}
  .opts{position:absolute;left:679px;top:537px;width:141px}
  .opts div{height:24.7px;display:flex;align-items:center;gap:10px;padding-left:5px;font-size:18px;letter-spacing:.4px}
  .opts div:nth-child(odd){background:var(--row-light)}
  .dot{display:inline-block;width:16px;height:16px;border:1.5px solid #444;border-radius:50%;background:#fff;flex:none}
  .grid{position:absolute;display:flex;gap:10px}
  .col{display:flex;flex-direction:column}
  .col div{height:30px;display:flex;align-items:center;gap:12px;padding-left:12px;font-size:18px;letter-spacing:.6px;color:#333}
  .col div:nth-child(odd){background:var(--row-dark)}
  .col div:nth-child(even){background:var(--row-light)}
  .blank{display:inline-block;border-bottom:1.3px solid #333;width:115px;height:14px}
  .state{position:absolute;left:44px;font-size:18px;letter-spacing:.5px;display:flex;align-items:center;gap:6px}
  .note{position:absolute;left:37px;width:780px;border-bottom:1.3px solid #333}
</style>
</head>
<body>
<div class="page">
  <div class="field" style="left:38px"><span>Date</span><span class="rule" style="width:278px"></span></div>
  <div class="field" style="left:385px"><span>Day of the Week</span><span class="rule" style="width:277px;margin-left:12px"></span></div>

  <div class="band" style="top:79px">TIME</div>
  <table class="time">
    <tr><td style="width:64px"></td><td style="width:89px">Begin</td><td style="width:81px">End</td><td style="width:146px">Duration</td><td style="width:46px"></td><td style="width:95px">Begin</td><td style="width:85px">End</td><td>Duration</td></tr>
    <tr><td>1</td><td></td><td></td><td></td><td>4</td><td></td><td></td><td></td></tr>
    <tr><td>2</td><td></td><td></td><td></td><td>5</td><td></td><td></td><td></td></tr>
    <tr><td>3</td><td></td><td></td><td></td><td>6</td><td></td><td></td><td></td></tr>
  </table>

  <div class="band" style="top:284px">SEVERITY OF PAIN (circle range)</div>
  <div class="scale">
    <div class="num" style="left:41px">1</div><div class="num" style="left:119px">2</div>
    <div class="num" style="left:197px">3</div><div class="num" style="left:275px">4</div>
    <div class="num" style="left:353px">5</div><div class="num" style="left:431px">6</div>
    <div class="num" style="left:509px">7</div><div class="num" style="left:587px">8</div>
    <div class="num" style="left:665px">9</div><div class="num" style="left:743px">10</div>
    <div class="face" style="left:119px" role="img" aria-label="Smiling face for mild pain"></div>
    <div class="face" style="left:275px" role="img" aria-label="Smiling face for moderate pain"></div>
    <div class="face" style="left:431px" role="img" aria-label="Frowning face for severe pain"></div>
    <div class="face" style="left:587px" role="img" aria-label="Frowning face for very severe pain"></div>
    <div class="face" style="left:743px" role="img" aria-label="Crying face for worst pain possible"></div>
    <div class="level" style="left:119px">Mild</div>
    <div class="level" style="left:275px">Moderate</div>
    <div class="level" style="left:431px">Severe</div>
    <div class="level" style="left:587px">Very Severe</div>
    <div class="level" style="left:743px;top:96px">Worst Pain<br>Possible</div>
  </div>

  <div class="band" style="top:477px">LOCATION</div>
  <div class="loc" style="left:80px" role="img" aria-label="Head profile with jaw joint highlighted"></div>
  <div class="loc" style="left:187px" role="img" aria-label="Head profile with muscles highlighted"></div>
  <div class="loc" style="left:289px" role="img" aria-label="Head profile with neck highlighted"></div>
  <div class="loc" style="left:380px" role="img" aria-label="Front of head with forehead tension highlighted"></div>
  <div class="loc" style="left:485px" role="img" aria-label="Set of teeth"></div>
  <div class="divider" style="left:131px"></div><div class="divider" style="left:236px"></div>
  <div class="divider" style="left:333px"></div><div class="divider" style="left:436px"></div>
  <div class="divider" style="left:535px"></div>
  <div class="loc-label" style="left:80px">Joint</div>
  <div class="loc-label" style="left:187px">Muscles</div>
  <div class="loc-label" style="left:292px">Neck</div>
  <div class="loc-label" style="left:381px">Tension</div>
  <div class="loc-label" style="left:485px">Teeth</div>
  <div class="q" style="top:546px">Click/Pop</div>
  <div class="q" style="top:626px">Opening<br>Ability</div>
  <div class="opts">
    <div><span class="dot"></span>Increased</div><div><span class="dot"></span>Decreased</div>
    <div><span class="dot"></span>No Change</div><div><span class="dot"></span>Incresed</div>
    <div><span class="dot"></span>Decreased</div><div><span class="dot"></span>No Change</div>
  </div>

  <div class="band" style="top:697px">TRIGGERS (Check all that apply)</div>
  <div class="grid" style="left:35px;top:743px">
    <div class="col" style="width:240px"><div><span class="dot"></span>Sleep</div><div><span class="dot"></span>Frist thing in AM</div><div><span class="dot"></span>Clenching</div><div><span class="dot"></span>Insomnia</div></div>
    <div class="col" style="width:264px"><div><span class="dot"></span>Weather</div><div><span class="dot"></span>Eating</div><div><span class="dot"></span>Work</div><div><span class="dot"></span>Opening Wild/yown</div></div>
    <div class="col" style="width:265px"><div><span class="dot"></span>PMS/Menstration</div><div><span class="dot"></span>Stress at Home</div><div><span class="dot"></span>Stress at Work</div><div><span class="dot"></span>Othet <span class="blank"></span></div></div>
  </div>
  <div class="state" style="top:870px">My Jaw was <span class="dot"></span> relaxed <span class="dot"></span> clenched <span class="dot"></span> my breathing was <span class="dot"></span> shallow/tense</div>
  <div class="state" style="top:896px">My neck/Shoulders were <span class="dot"></span> relaxed <span class="dot"></span> tense</div>

  <div class="band" style="top:924px">Relief Measures (Check all that apply)</div>
  <div class="grid" style="left:37px;top:970px">
    <div class="col" style="width:262px"><div><span class="dot"></span>Deep Breathing</div><div><span class="dot"></span>Teeth apart/Relax Jaw</div><div><span class="dot"></span>Self-Massage</div><div><span class="dot"></span>Heat/Cold (Circle)</div></div>
    <div class="col" style="width:262px"><div><span class="dot"></span>Medication</div><div><span class="dot"></span>Rest</div><div><span class="dot"></span>Gentle Stretching</div><div><span class="dot"></span>Posture Correction</div></div>
    <div class="col" style="width:241px"><div><span class="dot"></span>Mindful rest</div><div><span class="dot"></span>Stabilization Exercise</div><div><span class="dot"></span>Other <span class="blank" style="width:125px"></span></div><div><span class="dot"></span><span class="blank" style="width:178px"></span></div></div>
  </div>

  <div class="band" style="top:1097px">Notes and Plan to Avoid Triggevs</div>
  <div class="note" style="top:1168px"></div>
  <div class="note" style="top:1205px"></div>
  <div class="note" style="top:1241px"></div>
</div>
</body>
</html>
```